Design of two graphics from basic existing design & colours

I have two graphics which I currently use but they are nothing special. We would like to transform these two graphics, using our existing logo colour, into something special. The outputs will be used:

- on our website;
- in a powerpoint sales presentation;
- in email campaigns; and
- to print for handing to prospects at the end of a sales presentation.

Please just submit one of the graphics and if we like the design, we will ask you to work on the second graphic. These two graphics are critical to our marketing and will be used together so we need them to have a similar look and feel.

```html
<!DOCTYPE html>
<html lang="en">
<head>
<meta charset="utf-8">
<title>Advisory Board Management Cycle</title>
<link href="https://fonts.googleapis.com/css2?family=Open+Sans:wght@400;600&display=swap" rel="stylesheet">
<style>
  :root {
    --bg: #f4f4f2;
    --red: #c8202a;
    --black: #2b2b2b;
    --grey: #8e8e8e;
    --white: #ffffff;
  }
  * { margin: 0; padding: 0; box-sizing: border-box; }
  html, body { width: 1200px; height: 828px; overflow: hidden; background: var(--bg); }
  .cycle {
    position: relative;
    width: 1200px;
    height: 828px;
    font-family: "Open Sans", sans-serif;
  }
  .cycle-wheel { position: absolute; inset: 0; }
  .seg-red { fill: var(--red); }
  .seg-black { fill: var(--black); }
  .seg-grey { fill: var(--grey); }
  .turn-arrow { fill: none; stroke: var(--white); stroke-width: 5; stroke-linecap: round; }
  .turn-head { fill: var(--white); }
  .hub-line { stroke: var(--black); stroke-width: 1.5; }
  .hub-small { font-size: 12px; fill: var(--black); text-anchor: middle; }
  .hub-title { font-size: 15px; fill: var(--black); text-anchor: middle; }

  .step {
    position: absolute;
    width: 124px;
    height: 94px;
    transform: translate(-50%, -50%);
    display: flex;
    align-items: center;
    justify-content: center;
    text-align: center;
    font-size: 16px;
    line-height: 1.3;
    border: 2px solid;
    background: var(--bg);
    padding: 4px;
    white-space: nowrap;
  }
  .step-red { color: var(--red); border-color: var(--red); }
  .step-black { color: var(--black); border-color: var(--black); }
  .step-grey { color: var(--grey); border-color: var(--grey); }
</style>
</head>
<body>
<main class="cycle">
  <svg class="cycle-wheel" viewBox="0 0 1200 828" width="1200" height="828" aria-label="Management cycle wheel">
    <defs>
      <path id="segment" d="M -21.5 -75 L -41.3 -144.2 A 150 150 0 0 1 41.3 -144.2 L 21.5 -75 A 78 78 0 0 0 -21.5 -75 Z"/>
      <g id="turn">
        <path class="turn-arrow" d="M -15.6 -110.9 A 112 112 0 0 1 9 -111.6"/>
        <polygon class="turn-head" points="9,-120 22,-111 9,-102"/>
      </g>
      <polygon id="out-arrow" points="-6,-153 6,-153 6,-192 16,-192 0,-215 -16,-192 -6,-192"/>
    </defs>

    <g transform="translate(600 414)">
      <g class="out-arrows">
        <use href="#out-arrow" class="seg-red" transform="rotate(-5.8)"/>
        <use href="#out-arrow" class="seg-black" transform="rotate(26.5)"/>
        <use href="#out-arrow" class="seg-grey" transform="rotate(72.6)"/>
        <use href="#out-arrow" class="seg-red" transform="rotate(101.4)"/>
        <use href="#out-arrow" class="seg-black" transform="rotate(129.8)"/>
        <use href="#out-arrow" class="seg-red" transform="rotate(176.3)"/>
        <use href="#out-arrow" class="seg-black" transform="rotate(205.6)"/>
        <use href="#out-arrow" class="seg-grey" transform="rotate(250.3)"/>
        <use href="#out-arrow" class="seg-red" transform="rotate(278.4)"/>
        <use href="#out-arrow" class="seg-black" transform="rotate(308)"/>
      </g>
      <g class="segments">
        <use href="#segment" class="seg-red" transform="rotate(0)"/>
        <use href="#segment" class="seg-black" transform="rotate(36)"/>
        <use href="#segment" class="seg-grey" transform="rotate(72)"/>
        <use href="#segment" class="seg-red" transform="rotate(108)"/>
        <use href="#segment" class="seg-black" transform="rotate(144)"/>
        <use href="#segment" class="seg-red" transform="rotate(180)"/>
        <use href="#segment" class="seg-black" transform="rotate(216)"/>
        <use href="#segment" class="seg-grey" transform="rotate(252)"/>
        <use href="#segment" class="seg-red" transform="rotate(288)"/>
        <use href="#segment" class="seg-black" transform="rotate(324)"/>
      </g>
      <g class="turns">
        <use href="#turn" transform="rotate(0)"/>
        <use href="#turn" transform="rotate(36)"/>
        <use href="#turn" transform="rotate(72)"/>
        <use href="#turn" transform="rotate(108)"/>
        <use href="#turn" transform="rotate(144)"/>
        <use href="#turn" transform="rotate(180)"/>
        <use href="#turn" transform="rotate(216)"/>
        <use href="#turn" transform="rotate(252)"/>
        <use href="#turn" transform="rotate(288)"/>
        <use href="#turn" transform="rotate(324)"/>
      </g>
    </g>

    <g class="hub">
      <line class="hub-line" x1="425" y1="414" x2="538" y2="414"/>
      <line class="hub-line" x1="662" y1="414" x2="775" y2="414"/>
      <text class="hub-small" x="600" y="376">Managing</text>
      <text class="hub-small" x="600" y="392">Structure</text>
      <text class="hub-title" x="600" y="419">Advisory Board</text>
      <text class="hub-small" x="600" y="446">Managing</text>
      <text class="hub-small" x="600" y="462">Performance</text>
    </g>
  </svg>

  <div class="step step-red" style="left:570px; top:120px;">Strategic<br>Plan</div>
  <div class="step step-black" style="left:724px; top:166px;">Annual<br>Business<br>Plan</div>
  <div class="step step-grey" style="left:901px; top:320px;">Departmental<br>Plans</div>
  <div class="step step-red" style="left:894px; top:474px;">Annual<br>Performance<br>Objectives &amp;<br>KPIs</div>
  <div class="step step-black" style="left:838px; top:612px;">Monthly<br>Performance<br>Meetings</div>
  <div class="step step-red" style="left:619px; top:712px;">Individual<br>Performance<br>Plan</div>
  <div class="step step-black" style="left:465px; top:696px;">Individual<br>Development<br>Plan</div>
  <div class="step step-grey" style="left:313px; top:517px;">Succesion<br>Plan</div>
  <div class="step step-red" style="left:283px; top:367px;">Business<br>Reviews</div>
  <div class="step step-black" style="left:369px; top:248px;">Advisory<br>Board<br>Meetings</div>
</main>
</body>
</html>
```